Chinese citizens moving to SYDNEY!

We need an A5 size flier for our new business. We would like this to be a fold-out flyer (brochure-style, i.e. 4 sides - front cover, middle, back cover). Full colour print (or 4 colour if it can be done without compromising the look). We need two versions of the same flyer - one in Chinese and one in English. Same design and imagery, just different languages. Copy is attached with imagery (subject to change once we source high res images).

Target Market(s)

Chinese citizens looking to emigrate to Sydney AND Chinese citizens who have recently moved to Sydney.

Industry/Entity Type

Business

Font styles to use
Sans Serif

Colors
ec1f27
000000
ffffff
fece3e

Requirements
Must have
• The front cover of the flier must be clean looking and show just our business name and tag line, along with an image of Sydney Harbour (provided). Main information ideally to be spread across the 2 centre pages with the back page quite clean, but if the text is too small we could consider it being spread across the remaining 3 pages (i.e. centre of the brochure, then the back cover).
• We would like it to be a clean and easy to read design. Suggested colours are written in the brief.
• It would be ideal to have a designer who can read Mandarin so that they know which characters make up a headline, which characters should not be spaced over two rows of text etc.

```html
<!DOCTYPE html>
<html lang="en">
<head>
<meta charset="utf-8">
<title>Bright Harbour Concierge – Folded Flyer</title>
<link rel="stylesheet" href="https://fonts.googleapis.com/css2?family=Open+Sans:wght@400;600;700&display=swap">
<style>
  :root {
    --red: #ec1f27;
    --red-deep: #b5070d;
    --gold: #fece3e;
    --gold-deep: #d9a812;
    --black: #000000;
    --white: #ffffff;
    --ink: #1c1c1c;
    --sky-top: #6f8fd0;
    --sky-low: #b9cff0;
    --stage: #2e2e2e;
  }
  * { box-sizing: border-box; margin: 0; padding: 0; }
  html, body { width: 1200px; height: 789px; overflow: hidden; }
  body {
    background: var(--stage);
    font-family: "Open Sans", Arial, sans-serif;
    position: relative;
  }
  .spread {
    position: absolute;
    left: 105px; top: 45px;
    width: 990px; height: 700px;
    display: flex;
  }
  .page {
    position: relative;
    width: 495px; height: 700px;
    overflow: hidden;
  }

  /* ---------- Back cover ---------- */
  .back-photo {
    position: absolute; inset: 0;
    background: linear-gradient(180deg, var(--sky-top) 0%, #8eaae0 45%, var(--sky-low) 75%, #9fb4cf 100%);
  }
  .section-ribbon {
    position: absolute; left: 0; top: 58px;
  }
  .section-title {
    position: absolute; left: 22px; top: 64px;
    color: var(--white); font-weight: 600; font-size: 17px;
  }
  .service-list {
    position: absolute; left: 30px; top: 112px; width: 420px;
    list-style: none;
    color: var(--white); font-size: 13.5px; line-height: 1.3;
  }
  .service-list li {
    position: relative; padding-left: 22px; margin-bottom: 4px;
  }
  .service-list svg {
    position: absolute; left: 0; top: 3px;
  }
  .back-band {
    position: absolute; left: 0; bottom: 0;
  }
  .contact {
    position: absolute; right: 48px; top: 548px;
    list-style: none;
    color: var(--white); font-size: 15px; line-height: 1.55;
  }
  .contact li { display: flex; align-items: center; gap: 7px; }

  /* ---------- Front cover ---------- */
  .front-photo {
    position: absolute; inset: 0;
    background: linear-gradient(180deg, #c9b6d6 0%, #9fb9e2 25%, #5c6f86 45%, #7fa4cf 62%, #4f8cc4 80%, #3b6fa4 100%);
  }
  .front-gold {
    position: absolute; left: 0; top: 0;
  }
  .web-top {
    position: absolute; right: 22px; top: 18px;
    font-size: 11px; color: var(--ink);
  }
  .brand {
    position: absolute; left: 70px; top: 52px;
    font-weight: 700; font-size: 26px; color: var(--ink);
    line-height: 1.1;
  }
  .front-band {
    position: absolute; left: 0; bottom: 0;
  }
  .tagline {
    position: absolute; right: 30px; top: 560px;
    color: var(--white); font-weight: 600; font-size: 25px;
    line-height: 1.3; text-align: right;
  }
</style>
</head>
<body>
<main class="spread">

  <!-- Back cover -->
  <section class="page page-back">
    <div class="back-photo" role="img" aria-label="Photo of a smiling family of three outdoors by the harbour under a clear blue sky"></div>

    <svg class="section-ribbon" width="260" height="40" viewBox="0 0 260 40">
      <polygon points="0,0 240,0 222,40 0,40" fill="var(--red)"/>
      <polygon points="240,0 256,0 238,40 222,40" fill="var(--gold)"/>
    </svg>
    <h2 class="section-title">Health &amp; Lifestyle</h2>

    <ul class="service-list">
      <li><svg width="12" height="11" viewBox="0 0 12 11"><path d="M1 6 L4.5 9.5 L11 1" stroke="var(--red)" stroke-width="2" fill="none"/></svg>Compare health insurance options</li>
      <li><svg width="12" height="11" viewBox="0 0 12 11"><path d="M1 6 L4.5 9.5 L11 1" stroke="var(--red)" stroke-width="2" fill="none"/></svg>Recommend the best medical professionals – GP, Dentist, Acupuncture and more</li>
      <li><svg width="12" height="11" viewBox="0 0 12 11"><path d="M1 6 L4.5 9.5 L11 1" stroke="var(--red)" stroke-width="2" fill="none"/></svg>Recommend restaurants</li>
      <li><svg width="12" height="11" viewBox="0 0 12 11"><path d="M1 6 L4.5 9.5 L11 1" stroke="var(--red)" stroke-width="2" fill="none"/></svg>Suggest the best local parks to visit and other outdoor activities</li>
      <li><svg width="12" height="11" viewBox="0 0 12 11"><path d="M1 6 L4.5 9.5 L11 1" stroke="var(--red)" stroke-width="2" fill="none"/></svg>Explain local dangers such as Australian wildlife, beach safety and more</li>
      <li><svg width="12" height="11" viewBox="0 0 12 11"><path d="M1 6 L4.5 9.5 L11 1" stroke="var(--red)" stroke-width="2" fill="none"/></svg>Suggest family outings, recommend holiday destinations, plan children's birthday parties, play dates and more</li>
      <li><svg width="12" height="11" viewBox="0 0 12 11"><path d="M1 6 L4.5 9.5 L11 1" stroke="var(--red)" stroke-width="2" fill="none"/></svg>Arrange Private chauffers</li>
    </ul>

    <svg class="back-band" width="495" height="270" viewBox="0 0 495 270">
      <defs>
        <linearGradient id="redBack" x1="0" y1="0" x2="1" y2="1">
          <stop offset="0" stop-color="var(--red)"/>
          <stop offset="1" stop-color="var(--red-deep)"/>
        </linearGradient>
      </defs>
      <polygon points="0,150 180,95 260,60 495,0 495,270 0,270" fill="url(#redBack)"/>
    </svg>

    <ul class="contact">
      <li><svg width="13" height="13" viewBox="0 0 13 13"><circle cx="6.5" cy="6.5" r="5.5" stroke="var(--white)" fill="none" stroke-width="1.2"/><path d="M4.5 3.8 L5.6 3.8 L6 5.4 L5.3 6 Q6 7.4 7.2 7.9 L7.8 7.2 L9.2 7.6 L9.2 8.7 Q6.5 9.2 4.5 5.5 Z" fill="var(--white)"/></svg>0100 200 3000</li>
      <li><svg width="14" height="11" viewBox="0 0 14 11"><rect x="0.7" y="0.7" width="12.6" height="9.6" stroke="var(--white)" fill="none" stroke-width="1.2"/><path d="M1 1 L7 6 L13 1" stroke="var(--white)" fill="none" stroke-width="1.2"/></svg>info@brightharbour.com</li>
      <li><svg width="13" height="13" viewBox="0 0 13 13"><circle cx="6.5" cy="6.5" r="5.5" stroke="var(--white)" fill="none" stroke-width="1.2"/><ellipse cx="6.5" cy="6.5" rx="2.4" ry="5.5" stroke="var(--white)" fill="none" stroke-width="1"/><line x1="1" y1="6.5" x2="12" y2="6.5" stroke="var(--white)" stroke-width="1"/></svg>www.brightharbour.com</li>
    </ul>
  </section>

  <!-- Front cover -->
  <section class="page page-front">
    <div class="front-photo" role="img" aria-label="Photo of Sydney Harbour Bridge with the city skyline and harbour water at dusk"></div>

    <svg class="front-gold" width="495" height="150" viewBox="0 0 495 150">
      <defs>
        <linearGradient id="goldBand" x1="0" y1="0" x2="1" y2="0">
          <stop offset="0" stop-color="var(--gold-deep)"/>
          <stop offset="0.5" stop-color="var(--gold)"/>
          <stop offset="1" stop-color="var(--gold-deep)"/>
        </linearGradient>
      </defs>
      <polygon points="0,0 495,0 495,40 330,100 200,120 150,148 60,100 0,100" fill="url(#goldBand)"/>
    </svg>
    <p class="web-top">www.brightharbour.com</p>
    <h1 class="brand">Bright Harbour<br>Concierge</h1>

    <svg class="front-band" width="495" height="230" viewBox="0 0 495 230">
      <defs>
        <linearGradient id="redFront" x1="0" y1="0" x2="1" y2="1">
          <stop offset="0" stop-color="var(--red)"/>
          <stop offset="1" stop-color="var(--red-deep)"/>
        </linearGradient>
      </defs>
      <polygon points="0,110 120,70 250,75 390,10 495,0 495,230 0,230" fill="url(#redFront)"/>
    </svg>
    <p class="tagline">Sydney's Relocation<br>and Settlement Experts</p>
  </section>

</main>
</body>
</html>
```